Online Psychiatry business - Business Card

I need a business card design. The target audience is busy professionals of any field (this therapy appeals best to 24-35 year olds). It involves psychiatry by tele-medicine (or video-conference). Nothing on it should be a giveaway that it's about mental health. Professional design with silver or gold as the primary colors appeals to me. The card must be as simple and as uncluttered as possible. Some color and flowing design on the edge of the card appeals to me.
CrestMindLink.com should probably appear in the center of the card and stand out, i.e. bold lettering, and easy to read, no cursive, but Ariel Black. Some where below this, should appear "Too Busy to Take Care of Yourself? Think again." Since this isn't office based, I don't think an office address is necessary and limits clutter.
Information that does need to appear is my name: Gerald Whitcombe, MD
General phone number: 541-876-2209. I'm hoping to get an 24-hour answering service soon so leave a little room for this. In addition I want to include two email addresses:
CrestMindLink@maildrop-box.com and CrestMind247@maildrop-box.com
Updates

I like the designs. I would like someone to put the website in bold in the center

 as most have been doing with a smaller font reminder nearby saying "No time" etc.
but I'd like to put my name down in the corner with the rest of the contact material.
Black print against a white or grey background appeals to me, with darker silver artwork near the sides (simple abstract, like wavy lines or something you can one up with that works. 
thanks

I ve tried to provide as much feedback as possible given my time limits, so if you have extra questions, please feel free to email. I tried to attach a file of a business card I really like but make be difficult to actually manufacture. I'm going to send you a link to the photo. The card has a pull tab. There is not much information on the outside. In fact, if you were to design the outside, I would just print : Too Busy to Take Care of Yourself? Think Again.

When you pull the tab the remaining information is on the bottom half of the card. Please don't use the color pink!!!!
http://www.layoutgallerypost.com/2009/05/100-clever-card-ideas/
It is the 39th photo on the list, about 2/3ds of the way down the page. It is titled: Faltenkästli

#7 and #16 have an appeal to me, except for the dot patterns
Hope this helps

I'm running out of time and energy. I 've been trying to give do down the list and give  individual feedback but I won't be able to do that anymore.

So if you have any specific questions, write me, and again thank you for all your effort!!

I know i received your files, including your zip files, Plonix,

but Gideon, did you send me the files including ZIP on project 5914386?
thanks

Target Market(s)

Working professionals and executive, attorneys, etc.

Industry/Entity Type

Business

Logo Text

Don't Have Time to Take Care of Yourself? Think Again.

Logo styles of interest
Pictorial/Combination Logo
Wordmark Logo
Other font styles liked:
• Ariel Black appeals to me the most

Requirements
Must have
• Want to emphasize that the website must be obvious, easily found (The CrestMindLink.com)
For that reason i'd like the card to be white, and minimal decoration on one or both sides just to add some style and color
Nice to have
• A Very uncluttered, elegant design, and something that makes it stick in your head-doesn't everyone want the last?
Should not have
• Nothing on the card that give it away that this is about psychiatry, such as brain or other symbol, but also nothing that gives it away as a medical business, such as a stethoscope or red cross or anything.

```html
<!DOCTYPE html>
<html lang="en">
<head>
<meta charset="utf-8">
<title>CrestMindLink Business Card</title>
<link href="https://fonts.googleapis.com/css2?family=Archivo+Black&family=Roboto+Condensed:wght@700&family=Open+Sans:wght@400&display=swap" rel="stylesheet">
<style>
  :root {
    --stage-light: #b4b4b4;
    --stage-dark: #3a3a3a;
    --ink: #111111;
    --paper: #ffffff;
    --silver-1: #8f9092;
    --silver-2: #c9cacc;
    --silver-3: #f4f4f5;
    --silver-4: #a9aaad;
    --card-edge: #7d7e80;
  }
  * { box-sizing: border-box; margin: 0; padding: 0; }
  html, body { width: 1200px; height: 900px; overflow: hidden; }
  body {
    position: relative;
    background: linear-gradient(110deg, var(--stage-light) 0%, #9c9c9c 45%, var(--stage-dark) 100%);
  }
  .card {
    position: absolute;
    width: 520px;
    height: 300px;
    border-radius: 16px;
    overflow: hidden;
    box-shadow: 0 10px 24px rgba(0,0,0,0.35);
    border: 1px solid var(--card-edge);
  }
  .silver {
    background: linear-gradient(115deg,
      var(--silver-1) 0%, var(--silver-2) 22%, var(--silver-3) 38%,
      var(--silver-4) 52%, var(--silver-2) 68%, var(--silver-3) 80%, var(--silver-1) 100%);
  }
  .card-back {
    left: 110px;
    top: 110px;
    display: flex;
    align-items: center;
    justify-content: center;
  }
  .tagline {
    font-family: "Roboto Condensed", "Arial Narrow", sans-serif;
    font-weight: 700;
    font-size: 26px;
    line-height: 1.3;
    color: var(--ink);
    text-align: center;
  }
  .card-front {
    left: 570px;
    top: 480px;
    background: var(--paper);
  }
  .front-art {
    position: absolute;
    inset: 0;
    width: 100%;
    height: 100%;
  }
  .website {
    position: absolute;
    left: 0;
    right: 0;
    top: 88px;
    text-align: center;
    font-family: "Archivo Black", "Arial Black", sans-serif;
    font-size: 38px;
    color: var(--ink);
    letter-spacing: -0.5px;
  }
  .contact {
    position: absolute;
    left: 22px;
    bottom: 18px;
    color: var(--ink);
  }
  .contact-name {
    font-family: "Archivo Black", "Arial Black", sans-serif;
    font-size: 17px;
  }
  .contact-title {
    font-family: "Open Sans", Arial, sans-serif;
    font-size: 12px;
    margin: 2px 0 8px;
  }
  .contact-lines {
    font-family: "Open Sans", Arial, sans-serif;
    font-size: 12px;
    white-space: nowrap;
  }
</style>
</head>
<body>
  <section class="card card-back silver">
    <p class="tagline">Not Enough Time to Care For Yourself?<br>Think Again.</p>
  </section>

  <section class="card card-front">
    <svg class="front-art" viewBox="0 0 520 300" preserveAspectRatio="none" aria-hidden="true">
      <defs>
        <linearGradient id="silverBand" x1="0" y1="0" x2="1" y2="0.4">
          <stop offset="0" stop-color="#8f9092"/>
          <stop offset="0.22" stop-color="#c9cacc"/>
          <stop offset="0.4" stop-color="#f4f4f5"/>
          <stop offset="0.55" stop-color="#a9aaad"/>
          <stop offset="0.72" stop-color="#dcdcdd"/>
          <stop offset="1" stop-color="#8f9092"/>
        </linearGradient>
      </defs>
      <path d="M0 160 C 120 175, 300 215, 520 200 L520 300 L0 300 Z" fill="url(#silverBand)"/>
      <path d="M0 156 C 130 170, 310 210, 520 190 L520 206 C 320 222, 140 180, 0 162 Z" fill="#111111"/>
    </svg>
    <div class="website">CrestMindLink.com</div>
    <div class="contact">
      <p class="contact-name">Gerald Whitcombe</p>
      <p class="contact-title">MD General</p>
      <p class="contact-lines">541-876-2209 | CrestMindLink@maildrop-box.com | CrestMind247@maildrop-box.com</p>
    </div>
  </section>
</body>
</html>
```